Book cover for a sci fi book called The Velvet Assembly

Dear Pixel Harbor team,

I would need a book cover design for my sci fi book, 'The Velvet Assembly'.

I will start by briefing you about the book's content, then I would like to advice you about a few possible book cover scenarios that I could imagine having for the book, and on which I would like to ask you to work on.

Book abstract:

The velvet assembly is a technically developed and spiritually evolved society from a distant galaxy.

Main location the actions take place: Planet Earth, globalized world, former Northern Germany, a new isolated high tech city at the sea, called Lees, inhabitants from everywhere, one government, one religion.
• Year: 2093
• The Velvet Assembly: solar system with 7 suns. The inhabitans of the velvet assembly have no physical body, only energetical bodies. Only when visiting Earth, they can incarnate at will.

The action starts on planet Earth, where a group of 4 people, two women and two males, who meet through different circumstances and decide to follow together a spiritual and philiosophical path towards self development and evolution. They meet an incarnated master from the velvet assembly who leads their path. At the end of the books, they reach a form of enlightment and transcende to The Velvet Assembly, they only come to know at the end the truth about the real origin of their master.

For the book cover, no matter what ideas you choose, please use max three predominant colors for that, red, yellow and orange. The book cover should inspire warmth.

Suggestions for the design:
- an abstract sun
- a cosmic view of the velvet assembly
- an abstractized design of a sacred geometry shape
- sun in the upper left corner, shining with visible rays on the whole surface of the book cover, a group of 4 people with the female old master sitting by their side in the lower right corner
- an out of the box Ufo, please choose for example an asymmetrical shape, definately not the usual flying sorcer, departing from the velvet assembly solar system, cosmic view from above
- PLEASE FEEL FREE TO BRAINSTROM ON YOUR OWN IDEAS BASED ON WHAT THE BOOK ABSTRACT INSPIRED YOU

For any questions, I am atbyour disposal.

I am looking forward to your design, thank you in advance for that.

Kind regards,
Mira

Target Market(s)

Sci Fi enthusiasts
Philosophers

Font styles to use
Serif

Colors
fbee3e
ffc214
faa54b
f37122
f04a50

Requirements
Must have
• For the book cover, no matter what ideas you choose, please use max three predominant colors for that, red, yellow and orange and/or any derived hues. The book cover should inspire warmth.
• Suggestions for the design:
• - an abstract sun
• - a cosmic view of the velvet assembly
• - an abstractized design of a sacred geometry shape
• - sun in the upper left corner, shining with visible rays on the whole surface of the book cover, a group of 4 people with the female old master sitting by their side in the lower right corner
• - an out of the box Ufo, please choose for example an asymmetrical shape, definately not the usual flying sorcer, departing from the velvet assembly solar system, cosmic view from above
• - PLEASE FEEL FREE TO BRAINSTROM ON YOUR OWN IDEAS BASED ON WHAT THE BOOK ABSTRACT INSPIRED YOU
Nice to have
• Minimalistic and modern design
Should not have
• dark or grey shades
• phtographs

```html
<!DOCTYPE html>
<html lang="en">
<head>
<meta charset="utf-8">
<title>The Velvet Assembly — Mira</title>
<link rel="stylesheet" href="https://fonts.googleapis.com/css2?family=Quicksand:wght@300;400&display=swap">
<style>
  :root {
    --cover-orange: #ff8000;
    --ray-yellow: #ffe82a;
    --sun-yellow: #f2fb22;
    --sun-amber: #ffc214;
    --core-white: #ffffff;
    --title-white: #ffffff;
  }
  html, body {
    margin: 0;
    padding: 0;
    overflow: hidden;
    background: var(--cover-orange);
  }
  .cover {
    position: relative;
    width: 850px;
    height: 1200px;
    background: var(--cover-orange);
    overflow: hidden;
  }
  .rays {
    position: absolute;
    inset: 0;
  }
  .rays line {
    stroke: var(--ray-yellow);
    stroke-width: 1.3;
  }
  .sun-emblem {
    position: absolute;
    left: 99px;
    top: 272px;
    width: 660px;
    height: 660px;
    border-radius: 50%;
    background: radial-gradient(circle at 50% 50%,
      var(--core-white) 0 4.5%,
      var(--sun-yellow) 5% 45%,
      var(--sun-amber) 60%,
      rgba(255, 194, 20, 0) 72%);
  }
  .title {
    position: absolute;
    left: 0;
    right: 0;
    top: 44px;
    margin: 0;
    text-align: center;
    font-family: "Quicksand", sans-serif;
    font-weight: 300;
    font-size: 90px;
    line-height: 84px;
    letter-spacing: -1px;
    color: var(--title-white);
  }
  .title span { display: block; }
  .author {
    position: absolute;
    left: 0;
    right: 0;
    top: 1002px;
    margin: 0;
    text-align: center;
    font-family: "Quicksand", sans-serif;
    font-weight: 300;
    font-size: 72px;
    line-height: 90px;
    color: var(--title-white);
  }
</style>
</head>
<body>
  <main class="cover">
    <svg class="rays" width="850" height="1200" viewBox="0 0 850 1200" aria-hidden="true">
      <line x1="172" y1="7" x2="429" y2="602"/>
      <line x1="687" y1="7" x2="429" y2="602"/>
      <line x1="0" y1="415" x2="429" y2="602"/>
      <line x1="4" y1="781" x2="429" y2="602"/>
      <line x1="850" y1="421" x2="429" y2="602"/>
      <line x1="850" y1="775" x2="429" y2="602"/>
      <line x1="190" y1="1200" x2="429" y2="602"/>
      <line x1="684" y1="1200" x2="429" y2="602"/>
    </svg>

    <div class="sun-emblem" role="img" aria-label="Abstract sun in sacred geometry: a radiant yellow and amber star of rings, circles and pointed rays around a white core"></div>

    <h1 class="title"><span>The Velvet</span><span>Assembly</span></h1>
    <p class="author">Mira</p>
  </main>
</body>
</html>
```